Create a Flyer for a Darts Tournament

We need a Flyer for a Darts Tournament that is going to be organized by our darts department (logo attached). The name of the tournament is "3. KLW Dartsturnier". The Flyer should look modern, professional and in a way that everyone can see at the first impression that is has to do with dart sports. The logo of our department should be on the flyer as well. On the flyer we need an area where we can place some informations regarding the tournament (bullet points) etc. And a area where we can place informations regarding the registration progress (e.g. "Registration via E-Mail". Should fit well to our logo.

Target Market(s)

Darts Players for the Tournament

Font styles to use
Serif

Colors

Designer to choose colors to be used in the design.

Requirements
Must have
• Name of the Tournament, our Logo, place for some tournament details, link to our registration page (besucher.tv-halmerau.de). Should

```html
<!DOCTYPE html>
<html lang="de">
<head>
<meta charset="utf-8">
<title>3. KLW Dartsturnier</title>
<link href="https://fonts.googleapis.com/css2?family=Russo+One&display=swap" rel="stylesheet">
<style>
  :root {
    --page: #0a2a42;
    --navy: #0d3560;
    --deep: #0b3f73;
    --bright: #0aa6ea;
    --cyan: #1cb4f2;
    --ink: #123a68;
    --white: #ffffff;
  }
  * { margin: 0; padding: 0; box-sizing: border-box; }
  html, body { width: 923px; height: 1200px; overflow: hidden; background: var(--page); }
  body { font-family: "Russo One", "Arial Black", sans-serif; color: var(--white); }

  .flyer {
    position: absolute; left: 104px; top: 93px; width: 714px; height: 1013px;
    overflow: hidden;
    background: linear-gradient(180deg, #0f6fb5 0%, #0b8fd8 35%, #0a6ab0 62%, #0c3f70 100%);
  }
  .backdrop {
    position: absolute; inset: 0;
    background:
      radial-gradient(ellipse 55% 40% at 50% 30%, rgba(70,200,255,.55), transparent 70%),
      linear-gradient(115deg, rgba(20,90,150,.6) 0%, rgba(10,150,230,.2) 45%, rgba(13,53,96,.5) 100%);
  }
  .streak { position: absolute; inset: 0; }

  .club-mark {
    position: absolute; left: 0; width: 100%; top: 180px;
    display: flex; align-items: center; justify-content: center; gap: 14px;
    font-size: 54px; color: var(--white); letter-spacing: 2px;
  }
  .club-mark .dot { width: 34px; height: 34px; border-radius: 50%; background: var(--white); }

  .capacity { position: absolute; left: 445px; top: 324px; width: 200px; height: 74px; }
  .capacity svg { position: absolute; inset: 0; }
  .capacity .top, .capacity .bottom {
    position: absolute; left: 0; width: 100%; text-align: center; color: var(--cyan);
    font-variant: small-caps;
  }
  .capacity .top { top: -4px; font-size: 19px; left: 10px; }
  .capacity .bottom { bottom: -3px; font-size: 14px; left: -8px; }
  .capacity .num { position: absolute; left: 74px; top: 14px; font-size: 50px; line-height: 1; color: var(--bright); }

  .title-main {
    position: absolute; left: 0; width: 100%; top: 420px; text-align: center;
    font-size: 112px; line-height: 1; letter-spacing: 2px;
    text-shadow: 0 0 24px rgba(120,220,255,.7);
  }
  .title-band {
    position: absolute; left: 30px; right: 30px; top: 533px; height: 60px;
    background: rgba(60,190,250,.35);
  }
  .title-sub {
    position: absolute; left: 0; width: 100%; top: 536px; text-align: center;
    font-size: 55px; line-height: 1; letter-spacing: 1px;
    text-shadow: 0 0 16px rgba(120,220,255,.6);
  }

  .lower-panel {
    position: absolute; left: 0; right: 0; top: 594px; bottom: 0;
    background: linear-gradient(180deg, rgba(13,53,96,.75), rgba(13,53,96,.35));
  }

  .date {
    position: absolute; left: 132px; top: 620px; width: 450px; height: 44px;
    border: 2px solid var(--white); transform: skewX(-8deg);
    display: flex; align-items: center; justify-content: center;
    background: var(--navy);
  }
  .date span { transform: skewX(8deg); font-size: 29px; font-variant: small-caps; letter-spacing: 1px; }

  .chip {
    position: absolute; background: var(--bright); color: var(--ink);
    clip-path: polygon(5% 0, 100% 0, 95% 100%, 0 100%);
    display: flex; flex-direction: column; align-items: center; justify-content: center;
    font-variant: small-caps; line-height: 1.05;
  }
  .time { top: 670px; height: 55px; font-size: 20px; }
  .time .line2 { color: var(--white); }
  .time-entry { left: 115px; width: 231px; padding-left: 60px; }
  .time-start { left: 337px; width: 231px; }
  .time-entry svg { position: absolute; left: 22px; top: 10px; }

  .info { position: absolute; left: 0; width: 100%; text-align: center; font-variant: small-caps; }
  .info-1 { top: 738px; font-size: 21px; }
  .info-2 { top: 761px; font-size: 21px; }
  .info-3 { top: 788px; font-size: 22px; letter-spacing: 1px; }

  .phase-label { position: absolute; top: 826px; font-size: 19px; color: var(--cyan); font-variant: small-caps; text-align: center; }
  .phase-group { left: 120px; width: 226px; }
  .phase-ko { left: 348px; width: 227px; }
  .phase { top: 857px; height: 33px; font-size: 19px; flex-direction: row; }

  .contact-band {
    position: absolute; left: 0; right: 0; top: 909px; height: 80px;
    background: linear-gradient(90deg, rgba(10,120,180,.5), rgba(10,150,220,.45), rgba(10,120,180,.5));
  }
  .contact-label { position: absolute; top: 918px; font-size: 21px; text-align: center; font-variant: small-caps; }
  .contact-infos { left: 47px; width: 304px; }
  .contact-reg { left: 358px; width: 303px; }
  .link {
    position: absolute; top: 947px; height: 28px;
    border: 2px solid var(--white); transform: skewX(-8deg);
    display: flex; align-items: center; justify-content: center;
    background: var(--navy);
  }
  .link span { transform: skewX(8deg); font-size: 16px; text-transform: uppercase; }
  .link-infos { left: 50px; width: 298px; }
  .link-reg { left: 362px; width: 298px; }
</style>
</head>
<body>
  <main class="flyer">
    <div class="backdrop" role="img" aria-label="Blau getönte Aufnahme einer Dartscheibe mit Pfeilen und eines Spielers am Board"></div>
    <svg class="streak" width="714" height="1013" viewBox="0 0 714 1013" aria-hidden="true">
      <polygon points="0,0 200,0 40,740 0,760" fill="rgba(255,255,255,.06)"/>
      <polygon points="714,400 714,470 560,1013 530,1013" fill="rgba(40,190,255,.35)"/>
      <polygon points="714,520 714,560 600,1013 585,1013" fill="rgba(40,190,255,.25)"/>
    </svg>

    <div class="club-mark"><span class="dot"></span><span>KLW Darts</span></div>

    <div class="capacity">
      <svg width="200" height="74" viewBox="0 0 200 74" aria-hidden="true">
        <polyline points="40,6 15,6 0,68 25,68" fill="none" stroke="#1cb4f2" stroke-width="2"/>
        <polyline points="178,6 200,6 185,68 165,68" fill="none" stroke="#1cb4f2" stroke-width="2"/>
        <g fill="none" stroke="#1cb4f2" stroke-width="2">
          <circle cx="22" cy="30" r="3"/><circle cx="30" cy="27" r="3"/><circle cx="38" cy="30" r="3"/>
          <rect x="18" y="35" width="8" height="18" rx="2"/>
          <rect x="26" y="32" width="8" height="22" rx="2"/>
          <rect x="34" y="35" width="8" height="18" rx="2"/>
        </g>
      </svg>
      <div class="top">Maximal</div>
      <div class="num">48</div>
      <div class="bottom">Teilnehmer</div>
    </div>

    <h1>
      <span class="title-main">3. KLW</span>
      <span class="title-band"></span>
      <span class="title-sub">DARTSTURNIER</span>
    </h1>

    <div class="lower-panel"></div>

    <div class="date"><span>Samstag, 25.01.2025</span></div>

    <div class="chip time time-entry">
      <svg width="34" height="34" viewBox="0 0 34 34" aria-hidden="true">
        <circle cx="17" cy="17" r="14" fill="none" stroke="#123a68" stroke-width="4"/>
        <polyline points="15,9 15,19 23,19" fill="none" stroke="#123a68" stroke-width="4"/>
      </svg>
      <span>Einlass</span><span class="line2">16:00 Uhr</span>
    </div>
    <div class="chip time time-start"><span>Turnierbeginn</span><span class="line2">17:00 Uhr</span></div>

    <p class="info info-1">Steel-Darts-Hobbyturnier</p>
    <p class="info info-2">(keine Ligaspieler)</p>
    <p class="info info-3">SVZ in 88470 Halmerau-Tiefenbach</p>

    <div class="phase-label phase-group">Gruppenphase</div>
    <div class="phase-label phase-ko">KO-Phase</div>
    <div class="chip phase phase-group">301 | DO | BO3</div>
    <div class="chip phase phase-ko">501 | DO | BO5</div>

    <div class="contact-band"></div>
    <div class="contact-label contact-infos">Infos</div>
    <div class="contact-label contact-reg">Anmeldung</div>
    <div class="link link-infos"><span>darts.tv-halmerau.de</span></div>
    <div class="link link-reg"><span>besucher.tv-halmerau.de</span></div>
  </main>
</body>
</html>
```